Brill Insurance Agency - Business Cards

Hello, I am needing new trendy business cards for our Insurance Agency now that I have a new Logo. I have attached our new logo with several color options along with a business card design that I like. I am leaning towards burgundy and blue colors. I have attached our current business card. I have also attached a headshot of our company president, Martin Vale, that you can use if you wish. Thank you so much in advance for all the wonderful designs!!!!

Target Market(s)

We want to look very professional to potential customers and we also want to look very professional so insurance companies will want to contract with us to sell their product.

Industry/Entity Type

Insurance

Contact Information for Business Card

Martin Vale
mvale@brillagency.com
Business: 555-213-4087
Fax: 555-213-7751
Cell: 555-390-2618
Toll Free: 888-555-0194
42 W Elm Rd Butler, MO 64730
www.brillagency.net

Font styles to use
Serif
Sans Serif

Colors
0355a3
3277b5
f04a50
ec1f27

Requirements
Nice to have
• I love creativity. The more creative and balanced a business card design the more I will like it. I would like the card to be printed horizontally instead of vertically.
Should not have
• My project should not have the Allied Coverage Network logo. It is no longer used in the industry.

```html
<!DOCTYPE html>
<html lang="en">
<head>
<meta charset="utf-8">
<title>Brill Insurance Agency – Business Cards</title>
<link rel="stylesheet" href="https://fonts.googleapis.com/css2?family=Montserrat:wght@400;500;700;800&display=swap">
<style>
  :root {
    --teal: #0fa393;
    --teal-dark: #0b8a7c;
    --ink: #161616;
    --paper: #ffffff;
    --paper-shade: #f2f2f2;
    --backdrop: #d9d9d9;
  }
  * { box-sizing: border-box; margin: 0; padding: 0; }
  html, body {
    width: 1200px; height: 801px; overflow: hidden;
    background: radial-gradient(circle at 50% 45%, #e6e6e6 0%, var(--backdrop) 75%);
    font-family: "Montserrat", sans-serif;
  }
  .sheet {
    position: relative; width: 1200px; height: 801px;
    display: flex; align-items: center; justify-content: center; gap: 60px;
  }
  .card {
    position: relative; width: 520px; height: 297px;
    background: linear-gradient(135deg, var(--paper) 0%, var(--paper-shade) 100%);
    box-shadow: 0 18px 30px rgba(0,0,0,.16), 0 2px 4px rgba(0,0,0,.08);
    overflow: hidden;
  }
  .card-shapes { position: absolute; inset: 0; }

  /* front */
  .holder { position: absolute; right: 30px; top: 34px; text-align: right; color: var(--ink); }
  .holder-name { font-weight: 800; font-size: 22px; letter-spacing: .5px; }
  .holder-title { font-weight: 700; font-size: 11px; letter-spacing: 1.5px; margin-top: 2px; }

  .brand { position: absolute; display: flex; align-items: center; gap: 10px; color: var(--teal); }
  .brand-dot { border-radius: 50%; border: 3px solid var(--teal); flex: none; }
  .brand-name { font-weight: 700; text-transform: uppercase; line-height: 1.15; letter-spacing: .6px; }
  .front .brand { left: 34px; top: 112px; }
  .front .brand-dot { width: 28px; height: 28px; }
  .front .brand-name { font-size: 12px; padding-left: 10px; border-left: 1px solid #9a9a9a; }

  .contact { position: absolute; display: flex; align-items: center; gap: 8px; color: var(--teal); font-size: 10px; font-weight: 500; line-height: 1.3; }
  .contact-icon { width: 22px; height: 22px; background: var(--teal); display: flex; align-items: center; justify-content: center; flex: none; }
  .contact-phone { left: 108px; top: 214px; }
  .contact-mail { left: 338px; top: 214px; }
  .address { position: absolute; left: 108px; top: 256px; font-size: 9px; font-weight: 700; color: var(--ink); letter-spacing: .2px; }

  /* back */
  .back .mark { position: absolute; left: 70px; top: 62px; display: flex; align-items: center; gap: 18px; color: var(--ink); }
  .mark-ring { width: 96px; height: 96px; border-radius: 50%; border: 9px solid var(--ink); flex: none; }
  .mark-name { font-weight: 800; font-size: 19px; line-height: 1.15; text-transform: uppercase; letter-spacing: .5px; }
  .back .holder-name { position: absolute; right: 24px; top: 158px; color: var(--paper); font-size: 19px; font-weight: 800; letter-spacing: .5px; }
  .back .brand { left: 34px; top: 232px; }
  .back .brand-dot { width: 24px; height: 24px; }
  .back .brand-name { font-size: 11px; padding-left: 10px; border-left: 1px solid #9a9a9a; }
</style>
</head>
<body>
<main class="sheet">

  <section class="card front" aria-label="Card front">
    <svg class="card-shapes" viewBox="0 0 520 297" aria-hidden="true">
      <polygon points="230,0 520,0 520,196" fill="var(--teal)"/>
      <polygon points="330,0 520,0 520,120" fill="var(--teal-dark)" opacity=".35"/>
      <polygon points="96,206 520,178 520,242 96,244" fill="var(--ink)"/>
      <rect x="0" y="206" width="96" height="38" fill="var(--ink)"/>
    </svg>

    <div class="holder">
      <div class="holder-name">MARTIN VALE</div>
      <div class="holder-title">DIRECTOR</div>
    </div>

    <div class="brand">
      <span class="brand-dot"></span>
      <span class="brand-name">Brill Insurance<br>Agency</span>
    </div>

    <div class="contact contact-phone">
      <span class="contact-icon">
        <svg width="12" height="12" viewBox="0 0 24 24" aria-hidden="true"><path fill="#111" d="M6.6 10.8a15.1 15.1 0 0 0 6.6 6.6l2.2-2.2a1 1 0 0 1 1-.25 11.4 11.4 0 0 0 3.6.57 1 1 0 0 1 1 1V20a1 1 0 0 1-1 1A17 17 0 0 1 3 4a1 1 0 0 1 1-1h3.5a1 1 0 0 1 1 1c0 1.25.2 2.45.57 3.57a1 1 0 0 1-.25 1z"/></svg>
      </span>
      <span>555-213-4087<br>555-390-2618</span>
    </div>

    <div class="contact contact-mail">
      <span class="contact-icon">
        <svg width="12" height="12" viewBox="0 0 24 24" aria-hidden="true"><rect x="3" y="5" width="18" height="14" fill="#111"/><path d="M3 5l9 7 9-7" fill="none" stroke="#0fa393" stroke-width="1.5"/></svg>
      </span>
      <span>mvale@brillagency.com<br>888-555-0194</span>
    </div>

    <div class="address">ADDRESS - 42 W Elm Rd Harlow, MO 64099</div>
  </section>

  <section class="card back" aria-label="Card back">
    <svg class="card-shapes" viewBox="0 0 520 297" aria-hidden="true">
      <polygon points="290,150 520,118 520,186 262,200" fill="var(--teal)"/>
    </svg>

    <div class="mark">
      <span class="mark-ring"></span>
      <span class="mark-name">Brill Insurance<br>Agency</span>
    </div>

    <div class="holder-name">MARTIN VALE</div>

    <div class="brand">
      <span class="brand-dot"></span>
      <span class="brand-name">Brill Insurance<br>Agency</span>
    </div>
  </section>

</main>
</body>
</html>
```